Maplebrook Cremations Postcard

Postcards to explain our services. Modern yet professional remembering this is about people's loved one's. Use Poppins font and Century Gothic.

Target Market(s)

People who's loved ones are going to pass away.

Font styles to use
Sans Serif

Colors
33a6d7

Requirements
Must have
• Logo, website, all the information from the attachments.

```html
<!DOCTYPE html>
<html lang="en">
<head>
<meta charset="utf-8">
<title>Maplebrook Cremations Postcard</title>
<link rel="stylesheet" href="https://fonts.googleapis.com/css2?family=Poppins:wght@600;700;800&family=Questrial&display=swap">
<style>
  :root {
    --canvas: #e2e2e2;
    --blue: #33a6d7;
    --blue-bright: #1ea2e4;
    --blue-deep: #1589c9;
    --orange: #f7931e;
    --orange-deep: #ee5c10;
    --yellow: #fbc02d;
    --brown: #2e1e14;
    --ink: #1d2a3a;
    --white: #ffffff;
    --line: #c9c9c9;
  }
  * { box-sizing: border-box; margin: 0; padding: 0; }
  html, body { width: 1200px; height: 2400px; overflow: hidden; }
  body { background: var(--canvas); position: relative; font-family: "Questrial", sans-serif; }

  .card { position: absolute; left: 100px; width: 1000px; height: 714px; overflow: hidden; }
  .card-front { top: 426px; }
  .card-back { top: 1260px; background: var(--white); }

  /* Front */
  .beach-photo {
    position: absolute; inset: 0;
    background: linear-gradient(180deg, #7a6a5e 0%, #c98a3c 26%, #f0b040 40%, #b9782e 52%, #6f5a44 68%, #8a6d52 100%);
  }
  .front-waves { position: absolute; inset: 0; }
  .logo-tab {
    position: absolute; left: 128px; top: 0; width: 286px; height: 196px;
    background: var(--white); border-radius: 0 0 30px 30px;
    display: flex; flex-direction: column; align-items: center; justify-content: center; gap: 10px;
  }
  .brand-dot { width: 78px; height: 78px; border-radius: 50%; background: linear-gradient(180deg, var(--orange), var(--orange-deep)); }
  .brand-name { font-family: "Questrial", sans-serif; color: var(--blue-deep); font-size: 25px; letter-spacing: 2px; text-transform: uppercase; text-align: center; line-height: 1.1; }
  .brand-name.small { font-size: 18px; letter-spacing: 1.5px; }

  .headline { position: absolute; left: 48px; width: 446px; top: 220px; text-align: center; font-family: "Poppins", sans-serif; font-weight: 800; font-size: 51px; line-height: 62px; text-transform: uppercase; }
  .headline .accent { color: var(--blue-bright); }
  .headline .main { color: var(--orange); }
  .headline-rule { position: absolute; left: 84px; top: 436px; width: 380px; height: 2px; background: var(--white); }
  .headline-rule::after { content: ""; position: absolute; left: 140px; top: -2px; width: 100px; height: 5px; background: var(--blue-bright); border-radius: 3px; }
  .tagline { position: absolute; left: 48px; width: 446px; top: 452px; text-align: center; color: var(--white); font-size: 22px; line-height: 27px; }

  .price-badge {
    position: absolute; left: 603px; top: 285px; width: 262px; height: 262px; border-radius: 50%;
    background: radial-gradient(circle at 40% 30%, #5ccaf7, var(--blue-bright) 60%, var(--blue-deep));
    box-shadow: 0 10px 18px rgba(0,0,0,0.25);
    display: flex; flex-direction: column; align-items: center; justify-content: center; color: var(--white);
  }
  .price-badge::before { content: ""; position: absolute; inset: 12px; border-radius: 50%; border: 2px dashed rgba(20, 60, 110, 0.55); }
  .price { font-family: "Poppins", sans-serif; font-weight: 800; font-size: 74px; line-height: 1; }
  .price-note { font-family: "Poppins", sans-serif; font-weight: 600; font-size: 27px; margin-top: 6px; }

  .front-phone { position: absolute; left: 520px; width: 436px; top: 562px; text-align: center; color: var(--white); font-family: "Poppins", sans-serif; font-weight: 800; font-size: 54px; line-height: 1; }
  .front-web { position: absolute; left: 520px; top: 634px; width: 432px; height: 36px; border-radius: 18px; background: var(--blue-bright); color: var(--ink); font-size: 22px; display: flex; align-items: center; justify-content: center; letter-spacing: 0.3px; }

  /* Back */
  .back-shapes { position: absolute; inset: 0; }
  .services-label { position: absolute; left: 0; top: 25px; width: 248px; height: 48px; background: var(--blue-bright); border-radius: 0 24px 24px 0; color: var(--ink); font-family: "Poppins", sans-serif; font-weight: 800; font-size: 24px; display: flex; align-items: center; padding-left: 28px; }
  .services-list { position: absolute; left: 32px; top: 88px; list-style: none; color: var(--white); font-size: 19px; }
  .services-list li { height: 32px; display: flex; align-items: center; gap: 10px; }
  .services-list svg { width: 13px; height: 13px; flex: none; }
  .phone-bar { position: absolute; left: 0; top: 477px; width: 539px; height: 86px; border-radius: 0 43px 43px 0; background: linear-gradient(180deg, #4cc3f5, var(--blue-bright)); display: flex; align-items: center; padding-left: 30px; gap: 20px; }
  .phone-bar svg { width: 48px; height: 48px; }
  .phone-bar span { color: var(--white); font-family: "Poppins", sans-serif; font-weight: 800; font-size: 50px; }
  .contact-list { position: absolute; left: 36px; top: 604px; list-style: none; color: var(--white); font-family: "Poppins", sans-serif; font-weight: 600; font-size: 17px; }
  .contact-list li { height: 32px; display: flex; align-items: center; gap: 10px; }
  .contact-list svg { width: 14px; height: 14px; }
  .back-brand { position: absolute; left: 597px; top: 95px; width: 180px; display: flex; flex-direction: column; align-items: center; gap: 8px; }
  .back-brand .brand-dot { width: 62px; height: 62px; }
  .stamp-box { position: absolute; left: 845px; top: 94px; width: 105px; height: 117px; border: 1.5px solid #9a9a9a; }
  .address-line { position: absolute; left: 613px; width: 337px; height: 1.5px; background: var(--line); }
</style>
</head>
<body>

<section class="card card-front" aria-label="Postcard front">
  <div class="beach-photo" role="img" aria-label="Photo of a sunset over the sea with waves on a sandy beach"></div>
  <svg class="front-waves" viewBox="0 0 1000 714" aria-hidden="true">
    <defs>
      <linearGradient id="frontOrange" x1="0" y1="0" x2="1" y2="0">
        <stop offset="0" stop-color="#f9a825"/><stop offset="1" stop-color="#ef5a0f"/>
      </linearGradient>
      <linearGradient id="frontYellow" x1="0" y1="0" x2="1" y2="0">
        <stop offset="0" stop-color="#fcd02f"/><stop offset="1" stop-color="#f7931e"/>
      </linearGradient>
    </defs>
    <path d="M1000,480 C900,405 760,430 650,515 C580,568 510,600 430,625 C300,668 150,690 0,660 L0,714 L1000,714 Z" fill="url(#frontOrange)"/>
    <path d="M0,590 C90,690 260,714 420,690 C330,714 200,714 0,714 Z" fill="url(#frontYellow)"/>
    <path d="M48,0 L494,0 L494,519 C470,585 380,662 250,684 C150,700 45,648 0,565 L0,420 L48,412 Z" fill="#2e1e14" fill-opacity="0.8"/>
    <path d="M0,448 C28,565 130,640 245,633 C330,628 395,600 455,568" fill="none" stroke="#1ea2e4" stroke-width="20" stroke-linecap="round"/>
  </svg>

  <div class="logo-tab">
    <div class="brand-dot"></div>
    <div class="brand-name">Maplebrook<br>Cremations</div>
  </div>

  <h1 class="headline">
    <span class="accent">Online</span><br>
    <span class="main">Arrangement</span><br>
    <span class="main">Center</span>
  </h1>
  <div class="headline-rule"></div>
  <p class="tagline">Hand Delivery of Cremated Remains<br>Miami-Dade County</p>

  <div class="price-badge">
    <span class="price">$695</span>
    <span class="price-note">All-Inclusive</span>
  </div>

  <p class="front-phone">(305) 555-0142</p>
  <p class="front-web">WWW.MAPLEBROOKCREMATIONS.COM</p>
</section>

<section class="card card-back" aria-label="Postcard back">
  <svg class="back-shapes" viewBox="0 0 1000 714" aria-hidden="true">
    <defs>
      <linearGradient id="backOrange" x1="0" y1="0" x2="0.6" y2="1">
        <stop offset="0" stop-color="#f9a21d"/><stop offset="1" stop-color="#ee6410"/>
      </linearGradient>
    </defs>
    <path d="M0,0 L590,0 C620,80 610,220 555,340 C500,450 470,530 490,610 C510,670 580,702 660,714 L0,714 Z" fill="#1ea2e4"/>
    <path d="M0,0 L527,0 C560,60 560,200 500,330 C450,430 410,500 430,580 C445,650 480,690 520,714 L0,714 Z" fill="url(#backOrange)" stroke="#ffffff" stroke-width="6"/>
  </svg>

  <div class="services-label">OUR SERVICES</div>
  <ul class="services-list">
    <li><svg viewBox="0 0 14 14"><circle cx="7" cy="7" r="6" fill="none" stroke="#fff" stroke-width="1.3"/><path d="M4,7.2 L6.2,9.2 L10,5" fill="none" stroke="#fff" stroke-width="1.3"/></svg>Filing Death Certificate</li>
    <li><svg viewBox="0 0 14 14"><circle cx="7" cy="7" r="6" fill="none" stroke="#fff" stroke-width="1.3"/><path d="M4,7.2 L6.2,9.2 L10,5" fill="none" stroke="#fff" stroke-width="1.3"/></svg>Bringing Your Loved One into our Care</li>
    <li><svg viewBox="0 0 14 14"><circle cx="7" cy="7" r="6" fill="none" stroke="#fff" stroke-width="1.3"/><path d="M4,7.2 L6.2,9.2 L10,5" fill="none" stroke="#fff" stroke-width="1.3"/></svg>Refrigeration</li>
    <li><svg viewBox="0 0 14 14"><circle cx="7" cy="7" r="6" fill="none" stroke="#fff" stroke-width="1.3"/><path d="M4,7.2 L6.2,9.2 L10,5" fill="none" stroke="#fff" stroke-width="1.3"/></svg>Crematory Fee</li>
    <li><svg viewBox="0 0 14 14"><circle cx="7" cy="7" r="6" fill="none" stroke="#fff" stroke-width="1.3"/><path d="M4,7.2 L6.2,9.2 L10,5" fill="none" stroke="#fff" stroke-width="1.3"/></svg>Alternative Container (Cardboard)</li>
    <li><svg viewBox="0 0 14 14"><circle cx="7" cy="7" r="6" fill="none" stroke="#fff" stroke-width="1.3"/><path d="M4,7.2 L6.2,9.2 L10,5" fill="none" stroke="#fff" stroke-width="1.3"/></svg>Temporary Container (Cardboard)</li>
    <li><svg viewBox="0 0 14 14"><circle cx="7" cy="7" r="6" fill="none" stroke="#fff" stroke-width="1.3"/><path d="M4,7.2 L6.2,9.2 L10,5" fill="none" stroke="#fff" stroke-width="1.3"/></svg>Hand Delivery of Cremated Remains</li>
    <li><svg viewBox="0 0 14 14"><circle cx="7" cy="7" r="6" fill="none" stroke="#fff" stroke-width="1.3"/><path d="M4,7.2 L6.2,9.2 L10,5" fill="none" stroke="#fff" stroke-width="1.3"/></svg>Miami-Dade County</li>
    <li><svg viewBox="0 0 14 14"><circle cx="7" cy="7" r="6" fill="none" stroke="#fff" stroke-width="1.3"/><path d="M4,7.2 L6.2,9.2 L10,5" fill="none" stroke="#fff" stroke-width="1.3"/></svg>Medical Examiner Cremation Approval Fee</li>
    <li><svg viewBox="0 0 14 14"><circle cx="7" cy="7" r="6" fill="none" stroke="#fff" stroke-width="1.3"/><path d="M4,7.2 L6.2,9.2 L10,5" fill="none" stroke="#fff" stroke-width="1.3"/></svg>1st Copy of Death Certificate</li>
    <li><svg viewBox="0 0 14 14"><circle cx="7" cy="7" r="6" fill="none" stroke="#fff" stroke-width="1.3"/><path d="M4,7.2 L6.2,9.2 L10,5" fill="none" stroke="#fff" stroke-width="1.3"/></svg>Online Guestbook</li>
  </ul>

  <div class="phone-bar">
    <svg viewBox="0 0 48 48" aria-hidden="true">
      <path d="M10,6 C7,8 5,12 7,18 C11,30 20,39 32,42 C37,43 40,41 42,38 L36,31 C34,30 32,31 30,33 C24,30 19,25 16,19 C18,17 19,15 18,13 Z" fill="#1d2a3a"/>
      <path d="M28,10 A10,10 0 0 1 38,20 M28,4 A16,16 0 0 1 44,20" fill="none" stroke="#1d2a3a" stroke-width="2.5"/>
    </svg>
    <span>(305) 555-0142</span>
  </div>

  <ul class="contact-list">
    <li><svg viewBox="0 0 14 14"><rect x="1" y="3" width="12" height="8" fill="#1d2a3a"/><path d="M1,3 L7,8 L13,3" fill="none" stroke="#fff" stroke-width="1"/></svg>hello@maplebrookcremations.com</li>
    <li><svg viewBox="0 0 14 14"><circle cx="7" cy="7" r="6" fill="none" stroke="#1d2a3a" stroke-width="1.5"/><path d="M1,7 H13 M7,1 C4,4 4,10 7,13 C10,10 10,4 7,1" fill="none" stroke="#1d2a3a" stroke-width="1.2"/></svg>www.maplebrookcremations.com</li>
  </ul>

  <div class="back-brand">
    <div class="brand-dot"></div>
    <div class="brand-name small">Maplebrook<br>Cremations</div>
  </div>
  <div class="stamp-box"></div>
  <div class="address-line" style="top:323px"></div>
  <div class="address-line" style="top:395px"></div>
  <div class="address-line" style="top:465px"></div>
</section>

</body>
</html>
```